Corporate web site design for a blockchain oriented company

Design a web site for Tessaro. The company works on blockchain projects, mostly in B2B . Logo and content of the web site are attached with the project.

Corporate web sites means that we need to present the company and, at least, two of its projects.

Target Market(s)

B2B (Telecom, Gvt, online e-commerce web sites, banks, insurance ...)

Number of Pages Required

3 page

Font styles to use
Sans Serif

Requirements
Must have
• Landing page
• Page for KYC product
• Page for Loyalty product
• Team presentation
• Contact form
• Company presentation
• Several section can be in one page.
Nice to have
• Teaser video per project.
Should not have
• Heavy web site with a lot of animations.

```html
<!DOCTYPE html>
<html lang="en">
<head>
<meta charset="utf-8">
<title>Tessaro Technology</title>
<link href="https://fonts.googleapis.com/css2?family=Roboto:wght@300;400;500;700&family=Roboto+Condensed:wght@400;700&family=Oswald:wght@500;700&display=swap" rel="stylesheet">
<style>
:root{
  --ink:#2b2b2b;
  --dark:#333333;
  --text:#555555;
  --muted:#8a8a8a;
  --line:#cfcfcf;
  --light:#f0f0f0;
  --white:#ffffff;
  --contact:#3b3b3b;
}
*{box-sizing:border-box;margin:0;padding:0}
html,body{width:1200px;height:2643px;overflow:hidden;background:var(--white)}
body{position:relative;font-family:"Roboto",Arial,sans-serif;color:var(--text)}
section,header,footer{position:absolute;left:0;width:1200px}
.label-box{position:absolute;background:var(--dark);color:var(--white);font-family:"Roboto Condensed",Arial,sans-serif;font-weight:700;text-align:center;text-transform:uppercase;white-space:nowrap}
.ghost{position:absolute;left:0;width:1200px;text-align:center;font-family:"Oswald",Arial,sans-serif;font-weight:700;text-transform:uppercase;line-height:1}

/* top bar */
.topbar{top:0;height:35px;border-bottom:1px solid #e6e6e6;font-size:9px;color:var(--muted);letter-spacing:.3px}
.topbar .item{position:absolute;top:12px;display:flex;align-items:center;gap:5px;white-space:nowrap}
.topbar svg{width:9px;height:9px;fill:var(--muted)}
.topbar .socials{position:absolute;right:160px;top:12px;display:flex;gap:9px}
.topbar .socials span{width:8px;height:8px;border-radius:50%;background:#b5b5b5}

/* nav */
.navbar{top:35px;height:75px;box-shadow:0 2px 6px rgba(0,0,0,.06)}
.brand{position:absolute;left:162px;top:20px;display:flex;align-items:center;gap:12px;font-family:"Roboto",Arial,sans-serif;font-weight:500;font-size:30px;letter-spacing:3px;color:#111;text-transform:uppercase}
.brand .mark{width:22px;height:22px;border:2px solid #111}
.menu{position:absolute;right:160px;top:31px;display:flex;gap:31px;font-size:11px;font-weight:500;color:var(--ink);text-transform:uppercase}

/* hero */
.hero{top:110px;height:424px;background:linear-gradient(90deg,#8c8a87 0%,#b7b3ad 40%,#6e6a66 70%,#4a4643 100%)}
.hero-tag{left:162px;top:160px;width:310px;height:28px;line-height:28px;font-size:17px;font-weight:400;background:#2e2e2e}
.hero-title{position:absolute;left:160px;top:192px;font-family:"Oswald",Arial,sans-serif;font-weight:700;font-size:57px;line-height:1;color:var(--white);text-transform:uppercase;letter-spacing:-1px;white-space:nowrap}
.hero-sub{position:absolute;left:162px;top:255px;font-size:13px;color:#f2f2f2;text-transform:uppercase;letter-spacing:.3px}

/* about */
.about{top:534px;height:488px}
.about .ghost{top:62px;font-size:130px;color:#f3f3f3}
.about .label-box{left:528px;top:83px;width:143px;height:40px;line-height:40px;font-size:25px}
.pillar{position:absolute;top:146px;width:270px;text-align:center}
.pillar .ring{width:158px;height:158px;margin:0 auto;border:1px solid #444;border-radius:50%;display:flex;align-items:center;justify-content:center}
.pillar h3{margin-top:20px;font-size:17px;font-weight:500;color:var(--ink)}
.pillar p{margin-top:8px;font-size:11.5px;line-height:19px;color:#666}

/* kyc */
.kyc{top:1022px;height:478px;background:var(--light)}
.kyc .photo{position:absolute;left:0;top:0;width:550px;height:478px;background:linear-gradient(135deg,#c9c3b8 0%,#a19a8f 45%,#5d5a57 100%)}
.kyc .label-box{left:590px;top:51px;width:196px;height:37px;line-height:37px;font-size:22px}
.kyc .intro{position:absolute;left:592px;top:104px;width:445px;font-size:11px;line-height:17px;color:#555}
.feature{position:absolute;width:200px}
.feature h4{font-family:"Roboto Condensed",Arial,sans-serif;font-weight:700;font-size:13px;color:var(--ink);text-transform:uppercase;white-space:nowrap}
.feature p{margin-top:8px;font-size:10.5px;line-height:15px;color:#666}
.btn-outline{position:absolute;left:0;top:76px;width:86px;height:31px;border:1px solid #333;border-radius:3px;font-size:10px;font-weight:500;line-height:29px;text-align:center;color:var(--ink);text-transform:uppercase}

/* team */
.team{top:1500px;height:662px}
.team .ghost{top:60px;font-size:130px;color:#f3f3f3}
.team .eyebrow{position:absolute;left:0;width:1200px;top:75px;text-align:center;font-size:22px;font-weight:400;color:#555;text-transform:uppercase}
.team .label-box{left:492px;top:105px;width:216px;height:47px;line-height:47px;font-size:34px}
.team .intro{position:absolute;left:160px;top:163px;width:880px;text-align:center;font-size:11px;line-height:17px;color:#777}
.map{position:absolute;left:250px;top:140px;width:700px;height:390px;background:radial-gradient(ellipse at center,rgba(210,210,210,.35),rgba(255,255,255,0) 70%)}
.member{position:absolute;top:249px;width:240px;text-align:center}
.member .portrait{width:137px;height:137px;margin:0 auto;border-radius:50%;background:linear-gradient(160deg,#d8d4cf,#6d7480)}
.member h5{margin-top:15px;font-size:17px;font-weight:400;color:#444}
.member .role{margin-top:2px;font-size:11px;color:#888}
.member .call{margin-top:8px;font-family:"Roboto Condensed",Arial,sans-serif;font-weight:700;font-size:15px;color:#444}
.member .social{margin-top:15px;display:flex;justify-content:center;gap:4px}
.member .social span{width:35px;height:35px;border-radius:50%;border:2px solid #3b5ea8}
.member .social span:nth-child(2){border-color:#45a6e0}
.member .social span:nth-child(3){border-color:#2d76b3}
.member .social span:nth-child(4){border-color:#e02a2a}
.dots{position:absolute;top:570px;left:0;width:1200px;display:flex;justify-content:center;gap:3px}
.dots span{width:13px;height:13px;border-radius:50%;background:#d6d6d6}
.dots span:first-child{background:#666}

/* contact */
.contact{top:2162px;height:421px;background:linear-gradient(180deg,#3d3d3d,#353535)}
.contact .ghost{top:28px;font-size:150px;color:#474747}
.contact .label-box{left:162px;top:78px;width:352px;height:56px;line-height:56px;font-size:40px;text-align:left;padding-left:20px;background:#2a2a2a}
.field{position:absolute;height:24px;border-bottom:1px solid #9a9a9a;font-size:11px;letter-spacing:2px;color:#d8d8d8;text-transform:uppercase}
.field svg{position:absolute;right:4px;top:2px;width:13px;height:13px;fill:#cfcfcf}
.submit{position:absolute;left:162px;top:307px;width:115px;height:44px;border:1px solid #d0d0d0;border-radius:4px;color:var(--white);font-size:18px;letter-spacing:2px;line-height:42px;text-align:center;text-transform:uppercase}

/* footer */
.footer{top:2583px;height:60px;background:var(--white)}
.footer .copy{position:absolute;left:160px;top:24px;font-size:10px;letter-spacing:1.5px;color:#333;text-transform:uppercase}
.footer .social{position:absolute;right:160px;top:13px;display:flex;gap:7px}
.footer .social span{width:34px;height:34px;border-radius:50%;border:1.5px solid #333}
</style>
</head>
<body>

<header class="topbar">
  <div class="item" style="left:160px"><svg viewBox="0 0 10 10"><path d="M2 0l2 2-1 1.5c.7 1.4 1.9 2.6 3.5 3.5L8 6l2 2-1.5 2C4 9.5.5 6 0 1.5z"/></svg>+27 (0) 21 555 0148</div>
  <div class="item" style="left:330px"><svg viewBox="0 0 10 10"><path d="M0 2h10v6H0z"/></svg>INFO@TESSARO-TECH.COM</div>
  <div class="item" style="left:498px"><svg viewBox="0 0 10 10"><circle cx="5" cy="5" r="5"/></svg>WWW.TESSARO-TECH.COM</div>
  <div class="item" style="left:662px"><svg viewBox="0 0 10 10"><path d="M5 0a3.5 3.5 0 0 1 3.5 3.5C8.5 6 5 10 5 10S1.5 6 1.5 3.5A3.5 3.5 0 0 1 5 0z"/></svg>UNIT 4 HARBOUR ROW/PORT ELLIS/NORTHVALE</div>
  <div class="socials"><span></span><span></span><span></span><span></span></div>
</header>

<header class="navbar">
  <div class="brand">Tessaro <span class="mark"></span></div>
  <nav class="menu">
    <span>Home</span><span>About Us</span><span>KYC Poroduct</span><span>Loyalty Product</span><span>Team</span><span>Contact Us</span>
  </nav>
</header>

<section class="hero" role="img" aria-label="Smiling businessman working on a laptop in a bright office">
  <div class="label-box hero-tag">Solving Problems That Matter</div>
  <h1 class="hero-title">Tessaro Technology</h1>
  <p class="hero-sub">Create a collaborative environment for all organisation</p>
</section>

<section class="about">
  <div class="ghost">About</div>
  <div class="label-box">Tessaro</div>
  <div class="pillar" style="left:150px">
    <div class="ring">
      <svg width="90" height="80" viewBox="0 0 90 80" fill="none" stroke="#111" stroke-width="2.5" stroke-linecap="round" stroke-linejoin="round">
        <path d="M42 16a8 8 0 1 1 10 8c-3 1-4 3-4 6v3"/><circle cx="48" cy="40" r="1.5" fill="#111"/>
        <path d="M5 52h14l10-4h18a4 4 0 0 1 0 8H34M47 56l18-8a5 5 0 0 1 5 8L48 70H19l-14 0"/>
      </svg>
    </div>
    <h3>Why Tessaro?</h3>
    <p>Tessaro Technology is a technology enabler that pledges to tackle issues that have plagued organisations for years. The company is lead by a team with tremendous expertise ...</p>
  </div>
  <div class="pillar" style="left:457px">
    <div class="ring">
      <svg width="82" height="82" viewBox="0 0 82 82"><path fill="#333" d="M35 4h12l2 10 7 3 8-6 9 9-6 8 3 7 10 2v12l-10 2-3 7 6 8-9 9-8-6-7 3-2 10H35l-2-10-7-3-8 6-9-9 6-8-3-7-10-2V35l10-2 3-7-6-8 9-9 8 6 7-3z"/><circle cx="41" cy="41" r="14" fill="#fff"/></svg>
    </div>
    <h3>What can Tessaro do?</h3>
    <p>Currently, Tessaro is solving business problems using blockchain technology. If you have an issue that you would like to enquire, we would love to hear from you!</p>
  </div>
  <div class="pillar" style="left:763px">
    <div class="ring">
      <svg width="70" height="90" viewBox="0 0 70 90"><path fill="#111" d="M20 88V50L6 36c-4-4 1-10 6-6l10 9V8a4 4 0 0 1 8 0v28V4a4 4 0 0 1 8 0v32V8a4 4 0 0 1 8 0v30V16a4 4 0 0 1 8 0v40c0 14-6 22-12 26v6z"/><path fill="#fff" d="M24 62l8-8 10 4 6-4 4 4-8 8-8-2-6 6z"/></svg>
    </div>
    <h3>How can Tessaro help?</h3>
    <p>Tessaro technology leverages on the most advanced blockchain technology that might not be available a few years ago. If you are not sure if we can help you, you can contact us here!</p>
  </div>
</section>

<section class="kyc">
  <div class="photo" role="img" aria-label="Team of business colleagues laughing around a laptop at a meeting table"></div>
  <div class="label-box">What us KYC</div>
  <p class="intro">T-KYC is a compliance solution that facilitates real-time credential settlement in KYC processes. Account holders will be able to breeze through the typical sign-up procedures while not compromising security, achieving absolute control over one's own personal data.</p>
  <div class="feature" style="left:592px;top:180px">
    <h4>Virtual Identity (VID)</h4>
    <p>VIDs can be created by an account holder and each VID is paired with specific credentials</p>
    <div class="btn-outline">Learn More</div>
  </div>
  <div class="feature" style="left:851px;top:180px">
    <h4>Digital Signature</h4>
    <p>A digital signature from an authority shows that the particular credential is verified</p>
    <div class="btn-outline">Learn More</div>
  </div>
  <div class="feature" style="left:592px;top:313px">
    <h4>Distributed Ledger Technology</h4>
    <p>VIDs can be created by an account holder and each VID is paired with specific credentials</p>
    <div class="btn-outline">Learn More</div>
  </div>
  <div class="feature" style="left:851px;top:313px">
    <h4>Benefits of T-KYC</h4>
    <p>A digital signature from an authority shows that the particular credential is verified</p>
    <div class="btn-outline">Learn More</div>
  </div>
</section>

<section class="team">
  <div class="ghost">Team</div>
  <div class="map" role="img" aria-label="Faint dotted world map background"></div>
  <div class="eyebrow">Our Team</div>
  <div class="label-box">Member</div>
  <p class="intro">Nunc viverra velit placerat eros efficitur hendrerit. Curabitur metus turpis, tempor eget rhoncus et, consequat eget dolor. Suspendisse venenatis dolor eget venenatis placerat. Nulla eget tellus ut nunc facilisis scelerisque eget in nibh Nulla feugiat pretium nibh sed rutrum Mauris ullamcorper</p>
  <div class="member" style="left:176px">
    <div class="portrait" role="img" aria-label="Portrait of team advisor"></div>
    <h5>Daniel Reeve</h5><div class="role">Advisor</div><div class="call">CALL -011-555-20417</div>
    <div class="social"><span></span><span></span><span></span><span></span></div>
  </div>
  <div class="member" style="left:479px">
    <div class="portrait" role="img" aria-label="Portrait of team manager"></div>
    <h5>Marco Lindqvist</h5><div class="role">Manager</div><div class="call">CALL -011-555-20417</div>
    <div class="social"><span></span><span></span><span></span><span></span></div>
  </div>
  <div class="member" style="left:784px">
    <div class="portrait" role="img" aria-label="Portrait of project manager"></div>
    <h5>Elena Voss</h5><div class="role">Project Manager</div><div class="call">CALL -011-555-20417</div>
    <div class="social"><span></span><span></span><span></span><span></span></div>
  </div>
  <div class="dots"><span></span><span></span><span></span><span></span></div>
</section>

<section class="contact">
  <div class="ghost">Contact</div>
  <div class="label-box">Get in Touch</div>
  <div class="field" style="left:162px;top:170px;width:263px">Name<svg viewBox="0 0 12 12"><circle cx="6" cy="3.5" r="3"/><path d="M0 12c0-4 3-6 6-6s6 2 6 6z"/></svg></div>
  <div class="field" style="left:469px;top:170px;width:264px">Email<svg viewBox="0 0 12 12"><path d="M0 2h12v8H0z"/><path d="M0 2l6 5 6-5" stroke="#3d3d3d" fill="none"/></svg></div>
  <div class="field" style="left:775px;top:170px;width:266px">Phone<svg viewBox="0 0 12 12"><path d="M3 0h6v12H3z"/><path d="M4 1.5h4v8H4z" fill="#3d3d3d"/></svg></div>
  <div class="field" style="left:162px;top:252px;width:880px">Message<svg viewBox="0 0 12 12"><path d="M1 11l1-3 7-7 2 2-7 7z"/></svg></div>
  <div class="submit">Submit</div>
</section>

<footer class="footer">
  <div class="copy">Copyright Tessaro 2019. All rights reserved.</div>
  <div class="social"><span></span><span></span><span></span><span></span></div>
</footer>

</body>
</html>
```